Patternmaking service (fashion) card design

I need cards for my patternmaking service. I service both large and small fashion labels including ladies,mens and childrenswear. I would like cards that have a sort of vintage feel, especially 50's and 60's style. Pink is my signature colour. Its important to have a fashion reference of some kind.

Industry/Entity Type

Fashion

Contact Information for Business Card

Marigold Lantern, Patternmaking Service, Pennae Falcastro,
27 Wexbury Lane. Fernleigh Rise. QLD. 4127. 0415836204, email:spoolinda4@quillmail.example. "By appointment only"

```html
<!DOCTYPE html>
<html lang="en">
<head>
<meta charset="utf-8">
<title>Marigold Lantern – Patternmaking Service</title>
<link rel="stylesheet" href="https://fonts.googleapis.com/css2?family=Delius&family=Arimo:ital,wght@0,400;0,700;1,400&family=Cormorant+Garamond:ital,wght@1,500&display=swap">
<style>
  :root {
    --card-dark: #1d1d1d;
    --card-mid: #313131;
    --card-light: #3b3b3b;
    --pink: #f59acb;
    --pink-soft: #f2b3d6;
    --ink-white: #f1f1f1;
    --shadow: rgba(0, 0, 0, 0.9);
  }
  html, body {
    margin: 0;
    padding: 0;
    width: 1200px;
    height: 741px;
    overflow: hidden;
    background: var(--card-dark);
  }
  .card {
    position: relative;
    width: 1200px;
    height: 741px;
    overflow: hidden;
    background:
      radial-gradient(ellipse at 55% 45%, var(--card-light) 0%, var(--card-mid) 45%, var(--card-dark) 100%);
  }
  .decor {
    position: absolute;
    inset: 0;
    width: 1200px;
    height: 741px;
  }
  .brand,
  .service,
  .contact,
  .note {
    position: absolute;
    margin: 0;
    white-space: nowrap;
    text-shadow: 2px 3px 3px var(--shadow);
  }
  .brand {
    left: 156px;
    top: 136px;
    font-family: "Delius", sans-serif;
    font-weight: 400;
    font-size: 60px;
    line-height: 1;
    color: var(--pink);
    letter-spacing: 0.5px;
  }
  .service {
    left: 165px;
    top: 209px;
    font-family: "Arimo", sans-serif;
    font-size: 28px;
    line-height: 1.1;
    color: var(--ink-white);
  }
  .contact {
    left: 160px;
    top: 370px;
    font-family: "Arimo", sans-serif;
    font-style: italic;
    font-size: 30px;
    line-height: 39px;
    color: var(--pink);
  }
  .contact .person {
    display: block;
    font-style: normal;
    font-weight: 700;
    font-size: 27px;
    margin-left: 4px;
    margin-bottom: 3px;
  }
  .contact .line {
    display: block;
    margin-left: 8px;
  }
  .contact .phone {
    margin-left: 10px;
  }
  .contact .email {
    display: block;
    margin-left: 0;
    margin-top: 1px;
  }
  .note {
    left: 462px;
    top: 621px;
    font-family: "Cormorant Garamond", serif;
    font-style: italic;
    font-weight: 500;
    font-size: 30px;
    line-height: 1.1;
    color: var(--pink-soft);
  }
</style>
</head>
<body>
<main class="card">
  <svg class="decor" viewBox="0 0 1200 741">
    <defs>
      <radialGradient id="ornament-top">
        <stop offset="0" stop-color="#0c0c0c" stop-opacity="0.85"/>
        <stop offset="1" stop-color="#0c0c0c" stop-opacity="0"/>
      </radialGradient>
      <radialGradient id="ornament-bottom">
        <stop offset="0" stop-color="#0c0c0c" stop-opacity="0.8"/>
        <stop offset="1" stop-color="#0c0c0c" stop-opacity="0"/>
      </radialGradient>
      <linearGradient id="figure-tone" x1="0" y1="0" x2="0" y2="1">
        <stop offset="0" stop-color="#8a8a8a" stop-opacity="0.6"/>
        <stop offset="1" stop-color="#6a6a6a" stop-opacity="0.35"/>
      </linearGradient>
    </defs>
    <ellipse class="ornament-swirls-top" role="img" aria-label="Dark floral swirl ornament across the top left"
             cx="320" cy="40" rx="380" ry="260" fill="url(#ornament-top)"/>
    <ellipse class="ornament-swirls-bottom" role="img" aria-label="Dark floral swirl ornament along the bottom edge"
             cx="650" cy="741" rx="650" ry="180" fill="url(#ornament-bottom)"/>
    <rect class="fashion-figure" role="img" aria-label="Pale grey silhouette of a standing woman in a short dress"
          x="940" y="155" width="210" height="586" rx="80" fill="url(#figure-tone)"/>
  </svg>

  <h1 class="brand">Marigold Lantern</h1>
  <p class="service">Patternmaking Service</p>

  <address class="contact">
    <span class="person">Pennae Falcastro</span>
    <span class="line">27 Wexbury Lane. Fernleigh Rise.</span>
    <span class="line">QLD. 4127.</span>
    <span class="line phone">0415836204</span>
    <span class="email">spoolinda4@quillmail.example</span>
  </address>

  <p class="note">"By appointment only"</p>
</main>
</body>
</html>
```